Brightwell Renal Partners Brochure - Marketing brochure for a dialysis company in the USA

I want a brochure to be created for my business. I have a brochure that can be used as a comparison. My old Company name is Lone Mesa Renal Services. The new Company Name is Brightwell Renal Partners. I have a sample of the Old Brochure. and I uploaded the Logo of BRP. It will be used by my sales agents to introduce my company to potential client hospitals.

Target Market(s)

CEOs of Acute Hospitals and Medical Centers

Industry/Entity Type

Health Care

Requirements
Must have
• Use the sample as a guide. This project is for a 4 page brochure. (2 letter size pages folded in half crosswise) Use the text from the old brochure to the new brochure, replacing the old info with the new company info as needed.
Nice to have
• Here is my company info:
• Brightwell Renal Partners
• 4120 W 17th St
• Suite D
• It will be nice if the designer can give me the project files that would allow me to edit the text of the brochure.
• McAllen, TX 78519
• (956) 471-2283
• admin@BrightwellRenalLLC.com
• www.brightwellrenal.com

```html
<!DOCTYPE html>
<html lang="en">
<head>
<meta charset="utf-8">
<title>Brightwell Renal Partners – Brochure Spread</title>
<link href="https://fonts.googleapis.com/css2?family=Libre+Baskerville:wght@700&family=Lato:wght@400;700&family=Open+Sans:wght@700&display=swap" rel="stylesheet">
<style>
  :root {
    --red: #c8060c;
    --blue: #1a22b8;
    --green: #0f7a2a;
    --ink: #1d1d1d;
    --paper: #ffffff;
    --mist: #e4e4e4;
    --backdrop: #e8e6e2;
    --serif: "Libre Baskerville", "Times New Roman", serif;
    --sans: "Open Sans", Arial, sans-serif;
    --body: "Lato", Arial, sans-serif;
  }
  * { margin: 0; padding: 0; box-sizing: border-box; }
  html, body { width: 1200px; height: 907px; overflow: hidden; background: var(--backdrop); }

  .spread {
    position: absolute; left: 74px; top: 75px; width: 1054px; height: 753px;
    background: var(--paper); box-shadow: 0 4px 18px rgba(0,0,0,.18); overflow: hidden;
  }

  /* left page */
  .page-left { position: absolute; left: 0; top: 0; width: 509px; height: 753px; }
  .equipment-photo {
    position: absolute; left: 0; top: 0; width: 509px; height: 250px;
    background: linear-gradient(180deg, #d6d6d6 0%, #ececec 60%, rgba(255,255,255,0) 100%);
  }
  .about-title {
    position: absolute; left: 21px; top: 212px;
    font-family: var(--serif); font-size: 21px; color: var(--red); letter-spacing: .5px;
  }
  .about-copy {
    position: absolute; left: 22px; top: 246px; width: 462px;
    font-family: var(--body); font-size: 12.3px; line-height: 15px; color: var(--ink);
  }
  .brand-left { position: absolute; left: 26px; top: 553px; color: var(--blue); font-family: var(--serif); font-weight: 700; }
  .brand-left .mark { font-size: 52px; line-height: 54px; letter-spacing: -1px; }
  .brand-left .name { font-size: 11px; letter-spacing: .3px; }
  .divider { position: absolute; left: 226px; top: 545px; width: 1px; height: 108px; background: #b9b9b9; }
  .contact { position: absolute; left: 288px; top: 560px; font-family: var(--body); color: var(--ink); }
  .contact-row { display: flex; align-items: center; gap: 12px; height: 20px; }
  .contact-row.phone { font-family: var(--serif); font-size: 19px; height: 28px; margin-bottom: 6px; }
  .contact-row.web { font-size: 12px; font-weight: 700; }

  /* right page */
  .page-right { position: absolute; left: 509px; top: 0; width: 545px; height: 753px; }
  .page-right svg { position: absolute; left: 0; top: 0; }
  .brand-right { position: absolute; right: 24px; top: 24px; color: #fff; font-family: var(--serif); font-weight: 700; text-align: center; }
  .brand-right .mark { font-size: 54px; line-height: 56px; letter-spacing: -1px; }
  .brand-right .name { font-size: 10.5px; letter-spacing: .3px; }
  .headline { position: absolute; left: 27px; top: 560px; }
  .headline .line-1 { font-family: var(--serif); font-size: 23px; color: var(--blue); line-height: 30px; }
  .headline .line-2 { font-family: var(--serif); font-size: 23px; color: var(--green); line-height: 30px; }
  .headline .line-3 { font-family: var(--sans); font-size: 31px; color: var(--red); line-height: 42px; letter-spacing: .3px; }

  /* footer bands */
  .rule-red { position: absolute; left: 0; top: 674px; width: 1054px; height: 5px; background: var(--red); }
  .band-blue { position: absolute; left: 0; top: 688px; width: 1054px; height: 65px; background: var(--blue); }
  .cta {
    position: absolute; left: 509px; top: 688px; width: 545px; height: 65px;
    display: flex; align-items: center; justify-content: center;
    font-family: var(--serif); font-size: 32px; color: #fff;
  }
</style>
</head>
<body>
<main class="spread">
  <section class="page-left">
    <div class="equipment-photo" role="img" aria-label="Faded photo of dialysis machine controls"></div>
    <h2 class="about-title">ABOUT US</h2>
    <p class="about-copy">Lorem ipsum dolor sit amet, at cum primis viderer recteque. Animal voluptua dissentiunt per ad. Saperet perfecto indoctum vel cu, usu an iusto soleat. Eu eam wisi lucilius consectetuer.<br>Atqui ullum nemore te sed, sale viderer ad cum. Et eum wisi soluta disputando, est ex oratio sententiae temporibus. Te delectus definitiones sed. Id possit interpretaris qui, te nobis bonorum maiorum nam. Qui eu iuvaret feugiat invenire, ad nostrum nominavi vim.<br>Mel ad prima exerci nonumes, id atqui eruditi splendide has. Incorrupte sadipscing in nam. His ad primis explicari gubergren. Fabulas splendide pertinacia has eu, graece insolens gubergren pro ad. Vix at volutpat instructior, in vim audiam facilis copiosae, eripuit vocibus corpora duo id.<br>In ius justo possim accusamus, et sit quidam aliquam mentitum. In dicit verterem qualisque usu, sit ne mutat possit graeco, eu reque nonumy blandit mei. Sit omittam invidunt verterem ad, cu iuvaret legimus laoreet mel. Id sed elit aliquip, soleat veritus nominavi nec ex. Case accusamus voluptatibus nam in, luptatum salutandi neglegentur ea mei.</p>

    <div class="brand-left">
      <div class="mark">BRP</div>
      <div class="name">BRIGHTWELL RENAL PARTNERS</div>
    </div>
    <div class="divider"></div>
    <div class="contact">
      <div class="contact-row phone">
        <svg width="16" height="16" viewBox="0 0 16 16"><rect width="16" height="16" rx="2" fill="#c8060c"/><path d="M5 3.5c.6 0 1.1 1.6 1.1 2 0 .5-.9.7-.9 1.2.2 1.2 1.6 2.7 2.9 3 .5 0 .7-.9 1.2-.9.4 0 2 .5 2 1.1 0 .9-1 1.6-1.8 1.6C6.6 11.5 4 8.8 3.5 5.3 3.5 4.5 4.2 3.5 5 3.5z" fill="#fff"/></svg>
        0123456789
      </div>
      <div class="contact-row web">
        <svg width="16" height="12" viewBox="0 0 16 12"><rect x=".7" y=".7" width="14.6" height="10.6" fill="none" stroke="#c8060c" stroke-width="1.2"/><path d="M1 1l7 6 7-6" fill="none" stroke="#c8060c" stroke-width="1.2"/></svg>
        www.company@website.com
      </div>
      <div class="contact-row web">
        <svg width="16" height="16" viewBox="0 0 16 16"><circle cx="8" cy="8" r="6.5" fill="none" stroke="#c8060c" stroke-width="1.2"/><ellipse cx="8" cy="8" rx="3" ry="6.5" fill="none" stroke="#c8060c" stroke-width="1.1"/><path d="M1.5 8h13M2.5 4.5h11M2.5 11.5h11" stroke="#c8060c" stroke-width="1.1"/></svg>
        www.companywebsite.com
      </div>
    </div>
  </section>

  <section class="page-right">
    <svg width="545" height="753" viewBox="0 0 545 753">
      <path d="M0 0H545V470C470 200 260 40 0 55Z" fill="#c8060c"/>
      <path d="M0 116C240 95 450 190 545 505V540C380 530 190 522 0 505Z" fill="#c9c2bb" role="img" aria-label="Photo of a patient receiving dialysis with clinical staff"/>
      <path d="M0 68C260 52 470 210 545 482" fill="none" stroke="#fff" stroke-width="7"/>
      <path d="M0 81C260 68 470 225 545 495" fill="none" stroke="#1a22b8" stroke-width="14"/>
      <path d="M0 101C250 86 465 240 545 515" fill="none" stroke="#0f7a2a" stroke-width="11"/>
      <path d="M0 496C200 512 380 522 545 520" fill="none" stroke="#0f7a2a" stroke-width="9"/>
      <path d="M0 512C200 528 380 538 545 536" fill="none" stroke="#1a22b8" stroke-width="10"/>
      <circle cx="408" cy="505" r="92" fill="#fff"/>
      <circle cx="408" cy="505" r="84" fill="#c0212a" stroke="#0f7a2a" stroke-width="6" role="img" aria-label="Illustration of red blood cells"/>
    </svg>
    <div class="brand-right">
      <div class="mark">BRP</div>
      <div class="name">BRIGHTWELL RENAL PARTNERS</div>
    </div>
    <h1 class="headline">
      <div class="line-1">TIRED OF PAYING</div>
      <div class="line-2">OUTRAGEOUS PRICES</div>
      <div class="line-3">FOR INPATIENT DIALYSIS</div>
    </h1>
  </section>

  <div class="rule-red"></div>
  <div class="band-blue"></div>
  <div class="cta">CALL US NOW</div>
</main>
</body>
</html>
```